Wine Label: Corvinte

The project is to create 3 wine labels. The brand name is "Corvinte"

What we need is to have 3 versions: red wine, white wine and rose.

The wine is for young and modern people, between 21 and 31 years old, so it need to be casual, modern and fun, but at the same time it needs to keep the Premiums of a good European wine.

It is from Italy.

Target Market(s)

Young adults, between 21 and 31 years old. wine lovers

Requirements
Must have
• - Modern colors (Black, silver, red, etc.)
• - Clean label
• - Clear font
• - Style
• - The brand + the type of wine (red, white or rose)
Nice to have
• - A symbol to represent the brand
Should not have
• - Many elements
• - No clear fonts
• - No funny colors

```html
<!DOCTYPE html>
<html lang="en">
<head>
<meta charset="utf-8">
<title>Corvinte — Wine Labels</title>
<link rel="stylesheet" href="https://fonts.googleapis.com/css2?family=Bodoni+Moda:wght@400&family=Pinyon+Script&family=Playfair+Display:wght@700&display=swap">
<style>
  :root {
    --page: #ffffff;
    --silver: #a7aebb;
    --silver-light: #dfe3ea;
    --frame-dark: #4a4541;
    --ink-light: rgba(235, 222, 215, 0.72);
    --ink-script: #f1e6e2;

    --rose-deep: #553c46;
    --rose-mid: #745663;
    --rose-glow: #8a6a75;

    --white-deep: #5a4a38;
    --white-mid: #7c664d;
    --white-glow: #9c8363;

    --red-deep: #6a0e12;
    --red-mid: #94161c;
    --red-glow: #bd262b;
  }

  html, body {
    margin: 0;
    padding: 0;
    background: var(--page);
    overflow: hidden;
  }

  .canvas {
    position: relative;
    width: 1200px;
    height: 750px;
    overflow: hidden;
    background: var(--page);
  }

  .label--rose  { --deep: var(--rose-deep);  --mid: var(--rose-mid);  --glow: var(--rose-glow); }
  .label--white { --deep: var(--white-deep); --mid: var(--white-mid); --glow: var(--white-glow); }
  .label--red   { --deep: var(--red-deep);   --mid: var(--red-mid);   --glow: var(--red-glow); }

  .slot-1 { left: 63px; }
  .slot-2 { left: 433px; }
  .slot-3 { left: 803px; }
  .neck-slot-1 { left: 30px; }
  .neck-slot-2 { left: 410px; }
  .neck-slot-3 { left: 790px; }

  /* Front labels */
  .front-label {
    position: absolute;
    top: 62px;
    width: 335px;
    height: 466px;
    transform-origin: left top;
    transform: skewY(-5.5deg);
    background: radial-gradient(ellipse at 25% 55%, var(--glow) 0%, var(--mid) 50%, var(--deep) 100%);
    outline: 1px solid var(--frame-dark);
    overflow: hidden;
  }

  .front-label__photo {
    position: absolute;
    top: 0;
    bottom: 34px;
    left: 132px;
    right: 14px;
    border-radius: 0 0 46% 46% / 0 0 14% 14%;
    background:
      linear-gradient(180deg, rgba(0,0,0,0.18) 0%, rgba(255,255,255,0.05) 40%, rgba(255,255,255,0.12) 70%, rgba(255,255,255,0.06) 100%),
      linear-gradient(90deg, rgba(0,0,0,0.10) 0%, rgba(255,255,255,0.10) 50%, rgba(0,0,0,0.12) 100%);
  }

  .front-label__frame {
    position: absolute;
    inset: 6px;
    border: 1.5px solid var(--silver);
  }
  .front-label__frame::after {
    content: "";
    position: absolute;
    inset: 4px;
    border: 1px solid var(--silver-light);
    opacity: 0.8;
  }

  .front-label__brand {
    position: absolute;
    left: 34px;
    top: 262px;
    margin: 0;
    font-family: "Bodoni Moda", serif;
    font-weight: 400;
    font-size: 42px;
    line-height: 1;
    color: var(--ink-light);
    letter-spacing: -0.5px;
  }

  .front-label__variety {
    position: absolute;
    left: 160px;
    top: 303px;
    margin: 0;
    font-family: "Pinyon Script", cursive;
    font-size: 28px;
    line-height: 1;
    color: var(--ink-script);
  }

  .front-label__origin {
    position: absolute;
    left: 30px;
    width: 150px;
    top: 346px;
    margin: 0;
    text-align: center;
    font-family: "Pinyon Script", cursive;
    font-size: 16px;
    line-height: 18px;
    color: var(--ink-script);
  }

  .front-label__leaf {
    position: absolute;
    left: 88px;
    top: 386px;
    width: 36px;
    height: 26px;
    border-radius: 50% 40% 50% 45%;
    background: rgba(200, 160, 140, 0.3);
  }

  .front-label__abv {
    position: absolute;
    left: 22px;
    top: 438px;
    margin: 0;
    font-family: "Playfair Display", serif;
    font-weight: 700;
    font-size: 8.5px;
    color: var(--ink-script);
  }

  /* Neck labels */
  .neck-label {
    position: absolute;
    top: 585px;
    width: 372px;
    height: 124px;
  }
</style>
</head>
<body>
<main class="canvas">

  <section class="front-label label--rose slot-1">
    <div class="front-label__photo" role="img" aria-label="Photograph of a ballet dancer's feet en pointe"></div>
    <div class="front-label__frame"></div>
    <h2 class="front-label__brand">Corvinte</h2>
    <p class="front-label__variety">Rose</p>
    <p class="front-label__origin">Selected Italian Wine<br>2013</p>
    <div class="front-label__leaf" role="img" aria-label="Small vine leaf ornament"></div>
    <p class="front-label__abv">Alc. 14.9% by Vol.</p>
  </section>

  <section class="front-label label--white slot-2">
    <div class="front-label__photo" role="img" aria-label="Photograph of a ballet dancer's feet en pointe"></div>
    <div class="front-label__frame"></div>
    <h2 class="front-label__brand">Corvinte</h2>
    <p class="front-label__variety">White</p>
    <p class="front-label__origin">Selected Italian Wine<br>2013</p>
    <div class="front-label__leaf" role="img" aria-label="Small vine leaf ornament"></div>
    <p class="front-label__abv">Alc. 14.9% by Vol.</p>
  </section>

  <section class="front-label label--red slot-3">
    <div class="front-label__photo" role="img" aria-label="Photograph of a ballet dancer's feet en pointe"></div>
    <div class="front-label__frame"></div>
    <h2 class="front-label__brand">Corvinte</h2>
    <p class="front-label__variety">Red</p>
    <p class="front-label__origin">Selected Italian Wine<br>2013</p>
    <div class="front-label__leaf" role="img" aria-label="Small vine leaf ornament"></div>
    <p class="front-label__abv">Alc. 14.9% by Vol.</p>
  </section>

  <svg class="neck-label neck-slot-1" viewBox="0 0 372 124">
    <defs>
      <linearGradient id="neck-rose" x1="0" x2="1">
        <stop offset="0" stop-color="#553c46"/><stop offset="0.5" stop-color="#8a6a75"/><stop offset="1" stop-color="#553c46"/>
      </linearGradient>
      <radialGradient id="dancer-rose" cx="0.5" cy="0.45" r="0.5">
        <stop offset="0" stop-color="#b89aa4"/><stop offset="1" stop-color="#7a5c67"/>
      </radialGradient>
    </defs>
    <path d="M14,17 H358 Q358,29 371,29 V95 Q358,95 358,107 H14 Q14,95 1,95 V29 Q14,29 14,17 Z" fill="#4a4541"/>
    <path d="M20,23 H352 Q352,34 364,34 V90 Q352,90 352,101 H20 Q20,90 8,90 V34 Q20,34 20,23 Z" fill="url(#neck-rose)" stroke="#a7aebb" stroke-width="1.5"/>
    <ellipse cx="186" cy="62" rx="42" ry="60" fill="#4a4541"/>
    <ellipse cx="186" cy="62" rx="37" ry="55" fill="url(#neck-rose)" stroke="#a7aebb" stroke-width="1.5"/>
    <ellipse cx="186" cy="62" rx="31" ry="48" fill="url(#dancer-rose)" role="img" aria-label="Photograph of a ballerina in arabesque"/>
  </svg>

  <svg class="neck-label neck-slot-2" viewBox="0 0 372 124">
    <defs>
      <linearGradient id="neck-white" x1="0" x2="1">
        <stop offset="0" stop-color="#5a4a38"/><stop offset="0.5" stop-color="#9a8264"/><stop offset="1" stop-color="#5a4a38"/>
      </linearGradient>
      <radialGradient id="dancer-white" cx="0.5" cy="0.45" r="0.5">
        <stop offset="0" stop-color="#c2ab8c"/><stop offset="1" stop-color="#7c664d"/>
      </radialGradient>
    </defs>
    <path d="M14,17 H358 Q358,29 371,29 V95 Q358,95 358,107 H14 Q14,95 1,95 V29 Q14,29 14,17 Z" fill="#4a4541"/>
    <path d="M20,23 H352 Q352,34 364,34 V90 Q352,90 352,101 H20 Q20,90 8,90 V34 Q20,34 20,23 Z" fill="url(#neck-white)" stroke="#a7aebb" stroke-width="1.5"/>
    <ellipse cx="186" cy="62" rx="42" ry="60" fill="#4a4541"/>
    <ellipse cx="186" cy="62" rx="37" ry="55" fill="url(#neck-white)" stroke="#a7aebb" stroke-width="1.5"/>
    <ellipse cx="186" cy="62" rx="31" ry="48" fill="url(#dancer-white)" role="img" aria-label="Photograph of a ballerina in arabesque"/>
  </svg>

  <svg class="neck-label neck-slot-3" viewBox="0 0 372 124">
    <defs>
      <linearGradient id="neck-red" x1="0" x2="1">
        <stop offset="0" stop-color="#6a0e12"/><stop offset="0.5" stop-color="#b6232a"/><stop offset="1" stop-color="#6a0e12"/>
      </linearGradient>
      <radialGradient id="dancer-red" cx="0.5" cy="0.45" r="0.5">
        <stop offset="0" stop-color="#c9454a"/><stop offset="1" stop-color="#8a1419"/>
      </radialGradient>
    </defs>
    <path d="M14,17 H358 Q358,29 371,29 V95 Q358,95 358,107 H14 Q14,95 1,95 V29 Q14,29 14,17 Z" fill="#4a4541"/>
    <path d="M20,23 H352 Q352,34 364,34 V90 Q352,90 352,101 H20 Q20,90 8,90 V34 Q20,34 20,23 Z" fill="url(#neck-red)" stroke="#a7aebb" stroke-width="1.5"/>
    <ellipse cx="186" cy="62" rx="42" ry="60" fill="#4a4541"/>
    <ellipse cx="186" cy="62" rx="37" ry="55" fill="url(#neck-red)" stroke="#a7aebb" stroke-width="1.5"/>
    <ellipse cx="186" cy="62" rx="31" ry="48" fill="url(#dancer-red)" role="img" aria-label="Photograph of a ballerina in arabesque"/>
  </svg>

</main>
</body>
</html>
```